Community Management Company in need of WordPress templates for website redesign

We are a community association management company providing services to homeowner associations (HOAs), condominium associations, cooperatives, municipal utility districts, luxury high-rises and large master-planned communities within the Real Estate category.

We are looking to do a refresh of our site with newly-designed pages that are compatible with WordPress and can be uploaded to a domain with little complications.

We are interested in first having a landing page designed based on a specific audience and call to actions as described in the design brief file attached to this design project and pasted below:
Design Brief for VeldaCrest Website Refresh

General Details:
Company Name: VeldaCrest
Business Location: Carrollton, TX – HQ
Current website: www.veldacrest-example.com

Overview:

We are looking to for a refresh of our site with newly-designed pages that are compatible with WordPress and can be uploaded to a domain with little complications.

Our target audience / target market:
HOA and Association Board Members, Real Estate Builders & Developers, Residents and Homeowners, Vendors, Potential Business Partners

Project scope:
Create a landing page template with the target audience of HOA Board Members who are prospects of VeldaCrest
The goal of the landing page is to have them fill out the proposal form by having the page take them from our “why” message to our “how” and “what” messages so they are compelled to fill out the form. The new landing page needs to drive that behavior.
Our messages will include the following

Why messages:
• Because you deserve an exceptional community
• Because you and your residents deserve an exceptional lifestyle
• Because your community matters
• Because your residents matter
• Exceptional Community. Managed
• Exceptional Lifestyle. Delivered
How/What messages:

With over 25 years of experience, VeldaCrest provides exceptional community management solutions with the transparency and visibility your community deserves. Our fully integrated services are provided at competitive prices with the best people, best practices, and best cloud-based and mobile app technology.

Our team is made up of the industry’s leading experts equipped to answer your questions quickly. Our team includes: certified managers, degreed and certified accountants, experienced, multi-lingual customer service representatives, technology staff and industry executives. We perform industry leading best practices, on behalf of the communities we serve, ensuring you receive the highest level support, guidance and tools to assist in performing your fiduciary duties. With our proprietary, cloud-based and mobile app technology, pertinent community information is at your fingertips. You will be empowered to manage the business affairs of your community anytime, from any device, anywhere.

Our community management services include personalized onsite management, portfolio management, full-service community maintenance services, community management for builders and property developers, and Virtual CAM (Community Association Manager) management.

Our community communication services include cloud-based board, resident, closing, and attorney portals and mobile app technology, providing the transparency and visibility into the business affairs that your community deserves. In addition, we provide several communication tools to keep homeowners and residents informed via our community website, newsletter and event services.

VeldaCrest, one of the largest and fastest growing community management companies, is proud to provide exceptional services to hundreds of community associations from under 50 units to over 7,000 units in Arizona, California, Colorado, Florida, Georgia, Louisiana, Nevada, North Carolina, Oregon, Texas and Washington, including homeowner associations (HOAs), condominium associations, cooperatives, luxury high-rises, municipal utility districts and large master-planned communities.

Other page elements: additional content block/placeholders for:
• Link to Service description and technology pages
• Link to Mobile Apps page
• Request a proposal form fill content block
• Find an office form fill content block and link to local page upon completion of search via zip or state
• Contact us content block with information to include phone, email, fax, etc. and link to contact us landing page

Template Elements:
Files will also be uploaded including:
• Logo
• Colors
• Sales PPT for their reference

Please see attached design brief (file #4), logos (file #2&3), colors & branding standards (file #5) and a sales PPT deck (file #1) geared towards the audience for your reference.
Updates

Project Deadline Extended
Reason: I am extending the deadline by one week to give everyone a chance to provide updates based on the feedback and submissions. Thank you for all of your efforts. I look forward to seeing all of your designs.

Project Deadline Extended
Reason: Good day everyone, We are extending our deadline by one more week; so please continue to submit your designs and revisions. We look forward to seeing your work. Regards.

Thank you for all of your submissions.  I am in the process of getting votes tallied and should have some further information Tuesday of next week.

I am currently reviewing the votes and comments from the poll and will provide feedback within the next day; so please stay tuned.

We are conducting one more round of voting for the website refresh.  Once this is complete we will contact the finalists and make a selection shortly thereafter.  Thank you again for your participation.  Please stay tuned.

We are finalizing our 2nd poll and will request revisions, if appropriate.  Thank you.

Target Market(s)

HOA Board members per the design brief

Industry/Entity Type

Communication

Requirements
Must have
• focus on a landing page first; not the homepage design
Nice to have
• Please see design brief - File #4
Should not have
• home page elements for the time being.

```html
<!DOCTYPE html>
<html lang="en">
<head>
<meta charset="utf-8">
<title>VeldaCrest – Landing Page</title>
<link href="https://fonts.googleapis.com/css2?family=Ubuntu:wght@400;500;700&family=Noto+Serif:ital@1&display=swap" rel="stylesheet">
<style>
:root{
  --teal:#1d6a83;
  --teal-dark:#145468;
  --teal-deep:#0f4656;
  --green:#3f7a2c;
  --ink:#2b2b2b;
  --text:#444;
  --muted:#8a8a8a;
  --line:#d9d9d9;
  --footer:#f0f0f0;
  --white:#fff;
}
*{box-sizing:border-box;margin:0;padding:0}
html,body{width:1200px;height:2532px;overflow:hidden}
body{position:relative;background:var(--white);font-family:"Ubuntu",Arial,sans-serif;color:var(--text)}
.abs{position:absolute}

/* Hero */
.hero-photo{left:0;top:0;width:1200px;height:700px;
  background:linear-gradient(180deg,#cfe3ef 0%,#b9c9b4 30%,#9a7b5f 48%,#7d9b4e 70%,#6f9c3c 100%)}
.brand{left:144px;top:40px;display:flex;align-items:center;gap:12px}
.brand-mark{width:40px;height:40px;background:var(--teal)}
.brand-name{font-size:52px;font-weight:700;color:var(--teal);letter-spacing:-1px}
.brand-sub{left:330px;top:100px;font-size:14px;color:var(--teal)}
.band{left:0;top:560px}
.hero-title{left:0;top:720px;width:1200px;text-align:center;color:var(--white);text-transform:uppercase;font-weight:700}
.hero-title .line1{font-size:46px;letter-spacing:1px;line-height:60px}
.hero-title .line2{font-size:68px;letter-spacing:1px;line-height:80px}

.office{left:144px;top:519px;width:332px;height:166px;background:var(--white);box-shadow:0 2px 8px rgba(0,0,0,.25)}
.office-head{background:var(--teal);color:var(--white);padding:12px 16px 0;height:100px}
.office-head h3{font-size:20px;font-weight:700;letter-spacing:.3px;line-height:26px}
.office-head p{font-size:13px;line-height:17px;margin-top:6px}
.office-form{display:flex;gap:10px;padding:14px 16px 0}
.office-form .field{flex:1;height:36px;border:1px solid var(--line);background:var(--white);font-size:13px;color:var(--muted);padding:10px}
.btn{background:var(--teal-dark);color:var(--white);font-weight:700;font-size:14px;text-transform:uppercase;display:flex;align-items:center;justify-content:center}
.office-form .btn{width:100px;height:36px}

/* Intro */
.intro{left:139px;top:929px;width:920px;font-size:13px;line-height:21px}
.intro p+p{margin-top:18px}

/* Features */
.features{left:0;top:1418px;width:1200px;height:354px;background:linear-gradient(180deg,#fff 0%,#f4f4f4 100%)}
.feature{top:1452px;width:440px}
.feature h2{font-size:27px;font-weight:700;color:var(--ink);text-transform:uppercase;line-height:34px}
.feature p{font-size:14px;line-height:21px;margin-top:10px;height:180px}
.feature .btn{width:103px;height:30px;font-size:13px;font-weight:500;margin-top:44px}

/* Proposal */
.section-title{left:139px;top:1826px;font-size:27px;font-weight:700;color:var(--ink);text-transform:uppercase}
.input{border:1px solid var(--line);font-size:12px;color:var(--muted);padding:7px 12px;background:var(--white)}
.select::after{content:"";position:absolute;right:0;top:0;width:26px;height:100%;background:#e6e6e6}
.subhead{left:139px;top:2095px;font-family:"Noto Serif",Georgia,serif;font-style:italic;font-size:17px;color:var(--ink)}
.submit{left:962px;top:2190px;width:96px;height:30px;background:var(--green)}

/* Footer */
.footer{left:0;top:2266px;width:1200px;height:236px;background:var(--footer)}
.contact-title{left:139px;top:2300px;font-family:"Noto Serif",Georgia,serif;font-style:italic;font-size:17px;color:var(--ink)}
.hours{left:139px;top:2337px;font-size:13px;color:var(--muted)}
.contact-row{left:139px;font-size:12px;display:flex}
.contact-row dt{width:70px;font-weight:700;color:var(--ink)}
.contact-row dd{color:var(--teal)}
.foot-brand{left:865px;top:2300px;font-size:34px;font-weight:700;color:#9aa3a8}
.foot-brand-sub{left:960px;top:2342px;font-size:11px;color:#9aa3a8}
.social{left:866px;top:2390px;display:flex;gap:7px}
.social span{width:30px;height:30px;background:#3a3a3a}
.copyright{left:0;top:2502px;width:1200px;height:30px;background:var(--teal-deep);color:var(--white);font-size:12px;text-align:center;line-height:30px}
</style>
</head>
<body>

<div class="abs hero-photo" role="img" aria-label="Photograph of a smiling family of four sitting on the lawn in front of a brick suburban house"></div>

<div class="abs brand"><span class="brand-mark"></span><span class="brand-name">VeldaCrest</span></div>
<div class="abs brand-sub">Powered by LinkHaven</div>

<svg class="abs band" width="1200" height="340" viewBox="0 0 1200 340" aria-hidden="true">
  <path d="M0 60 C300 -10 700 -20 1200 60 L1200 340 L0 340 Z" fill="#1d6a83" opacity=".45"/>
  <path d="M0 105 C300 55 800 45 1200 100 L1200 340 L0 340 Z" fill="#1d6a83"/>
  <path d="M0 115 C300 70 800 60 1200 112 L1200 140 C800 90 300 95 0 140 Z" fill="#2a7d97" opacity=".5"/>
</svg>
<svg class="abs" style="left:582px;top:898px" width="36" height="18" aria-hidden="true"><path d="M0 0 L36 0 L18 18 Z" fill="#1d6a83"/></svg>

<h1 class="abs hero-title"><span class="line1">Because you deserve an</span><br><span class="line2">Exceptional Community</span></h1>

<div class="abs office">
  <div class="office-head">
    <h3>FIND A VELDACREST OFFICE</h3>
    <p>Find a VeldaCrest office nearest you by<br>entering your zip code</p>
  </div>
  <div class="office-form"><div class="field">Zip Code</div><div class="btn">Submit</div></div>
</div>

<div class="abs intro">
  <p>With over 25 years of experience, VeldaCrest provides exceptional community management solutions with the transparency and visibility your community deserves. Our fully integrated services are provided at competitive prices with the best people, best practices, and best cloud-based and mobile app technology.</p>
  <p>Our team is made up of the industry’s leading experts equipped to answer your questions quickly. Our team includes: certified managers, degreed and certified accountants, experienced, multi-lingual customer service representatives, technology staff and industry executives. We perform industry leading best practices, on behalf of the communities we serve, ensuring you receive the highest level support, guidance and tools to assist in performing your fiduciary duties. With our proprietary, cloud-based and mobile app technology, pertinent community information is at your fingertips. You will be empowered to manage the business affairs of your community anytime, from any device, anywhere.</p>
  <p>Our community management services include personalized onsite management, portfolio management, full-service community maintenance services, community management for builders and property developers, and Virtual CAM (Community Association Manager) management.</p>
  <p>Our community communication services include cloud-based board, resident, closing, and attorney portals and mobile app technology, providing the transparency and visibility into the business affairs that your community deserves. In addition, we provide several communication tools to keep homeowners and residents informed via our community website, newsletter and event services.</p>
  <p>VeldaCrest, one of the largest and fastest growing community management companies, is proud to provide exceptional services to hundreds of community associations from under 50 units to over 7,000 units in Arizona, California, Colorado, Florida, Georgia, Louisiana, Nevada, North Carolina, Oregon, Texas and Washington, including homeowner associations (HOAs), condominium associations, cooperatives, luxury high-rises, municipal utility districts and large master-planned communities.</p>
</div>

<div class="abs features"></div>
<section class="abs feature" style="left:139px">
  <h2>Services</h2>
  <p>Our HOA management services are a unique set of capabilities that include a bundle of services that are all fully integrated into our best people, best practices and best technology approach to managing your community to ensure the fullest possible community development. Our HOA management services enhance your level of community development, a concept we define as when a community operates at its peak potential in terms of financial and operational aspects as well as a deep sense of community spirit.</p>
  <div class="btn">Read More</div>
</section>
<section class="abs feature" style="left:628px">
  <h2>Mobile Apps</h2>
  <p>Lorem Ipsum is simply dummy text of the printing and typesetting industry. Lorem Ipsum has been the industry's standard dummy text ever since the 1500s, when an unknown printer took a galley of type and scrambled it to make a type specimen book. It has survived not only five centuries, but also the leap into electronic typesetting, remaining essentially unchanged. It was popularised in the 1960s with the release of Veltrane sheets containing Lorem Ipsum.</p>
  <div class="btn">Read More</div>
</section>

<h2 class="abs section-title">Request a Proposal</h2>
<div class="abs input" style="left:139px;top:1876px;width:456px;height:30px">First Name:</div>
<div class="abs input" style="left:603px;top:1876px;width:215px;height:30px">City:</div>
<div class="abs input" style="left:833px;top:1876px;width:225px;height:30px">State/Province:</div>
<div class="abs input" style="left:139px;top:1919px;width:456px;height:30px">Last Name:</div>
<div class="abs input" style="left:603px;top:1919px;width:215px;height:30px">Email:</div>
<div class="abs input" style="left:833px;top:1919px;width:225px;height:30px">Confirm Email:</div>
<div class="abs input" style="left:139px;top:1962px;width:456px;height:30px">Title:</div>
<div class="abs input" style="left:603px;top:1962px;width:215px;height:30px">Phone:</div>
<div class="abs input" style="left:833px;top:1962px;width:225px;height:30px">Best time to contact:</div>
<div class="abs input" style="left:139px;top:2005px;width:456px;height:64px">Address:</div>
<div class="abs input select" style="left:603px;top:2005px;width:455px;height:30px">How did you hear about us?</div>
<div class="abs input" style="left:603px;top:2045px;width:455px;height:30px">Name of Referral Source</div>

<h3 class="abs subhead">Community Information</h3>
<div class="abs input" style="left:139px;top:2148px;width:456px;height:30px">Name of Community :</div>
<div class="abs input select" style="left:603px;top:2148px;width:455px;height:30px">Type of Community:</div>
<div class="abs input" style="left:139px;top:2190px;width:456px;height:30px">Of Homes:</div>
<div class="abs btn submit">Submit</div>

<footer class="abs footer"></footer>
<h3 class="abs contact-title">Contact Us</h3>
<p class="abs hours">We are open from 7:30 a.m. - 7:00 p.m. Central time, Monday through Friday.</p>
<dl class="abs contact-row" style="top:2372px"><dt>PHONE:</dt><dd>555-4-VeldaCare (555-483-2273)</dd></dl>
<dl class="abs contact-row" style="top:2400px"><dt>FAX:</dt><dd>555-919-0147</dd></dl>
<dl class="abs contact-row" style="top:2428px"><dt>EMAIL:</dt><dd>SERVICE@VELDACREST-EXAMPLE.COM</dd></dl>
<div class="abs foot-brand">VeldaCrest</div>
<div class="abs foot-brand-sub">Powered by LinkHaven</div>
<div class="abs social" aria-label="Social links"><span></span><span></span><span></span><span></span><span></span><span></span></div>
<div class="abs copyright">© 2014 VeldaCrest LLC. All rights reserved.</div>

</body>
</html>
```